Ad Banner for knowledge management portal - Promote Knowledge Submission

This banner is used in knowledge management web site.

1. Banner size: 940x380
2. Business background: Provides maintenance, design and engineering, construction, machinery operation, material procurement and production management services for petrochemical and refinery business
3. We would like to see designs that
- Promote the benefits of sharing "Lesson Learned".
- Use the keyword "I will do it better if I have to do it again"
- Promote employees to submit "Lesson Learned". It is a lesson learned from work, submitted using a predefined form template.
- Promote a campaign that will give out souvenir for all employees who submit "Lesson Learned"
- Has the message "Click here to learn more about Lesson Learned"

Requirements
Must have
• Must have a picture of technician examining machine or equipments (using cartoon character)
Should not have
• Should not include picture of real people in the design

```html
<!DOCTYPE html>
<html lang="en">
<head>
<meta charset="utf-8">
<title>Lesson Learned – Knowledge Sharing Banner</title>
<link rel="stylesheet" href="https://fonts.googleapis.com/css2?family=Anton&family=Arimo:wght@400;700&display=swap">
<style>
  :root {
    --sky-deep: #1f5fc4;
    --sky-mid: #3c8fe6;
    --sky-light: #a9dcf8;
    --sky-glow: #e3f5fe;
    --ink-navy: #0d1a2e;
    --white: #ffffff;
    --button-top: #2c8ff0;
    --button-bottom: #0b63d4;
    --button-rim: #0a2a66;
    --figure-top: #c9d9ea;
    --figure-bottom: #2a2a2a;
  }
  * { box-sizing: border-box; margin: 0; padding: 0; }
  html, body {
    width: 1200px;
    height: 485px;
    overflow: hidden;
    background: #ffffff;
  }
  .banner {
    position: relative;
    width: 1200px;
    height: 485px;
    overflow: hidden;
    background:
      radial-gradient(ellipse 620px 380px at 820px 150px, var(--sky-glow) 0%, rgba(227,245,254,0) 70%),
      linear-gradient(100deg, var(--sky-deep) 0%, var(--sky-mid) 38%, var(--sky-light) 70%, var(--sky-mid) 100%);
  }
  .banner__waves {
    position: absolute;
    inset: 0;
    width: 1200px;
    height: 485px;
  }
  .headline {
    position: absolute;
    left: 44px;
    top: 56px;
    font-family: "Anton", "Impact", sans-serif;
    font-weight: 400;
    font-size: 118px;
    line-height: 1;
    letter-spacing: 4px;
    white-space: nowrap;
  }
  .headline__lead { color: var(--white); }
  .headline__tail { color: var(--ink-navy); }
  .tagline {
    position: absolute;
    left: 44px;
    top: 200px;
    font-family: "Arimo", "Arial", sans-serif;
    font-size: 44px;
    letter-spacing: 0;
    color: var(--ink-navy);
    white-space: nowrap;
  }
  .tagline__accent { color: var(--white); }
  .cta {
    position: absolute;
    left: 28px;
    top: 372px;
    width: 548px;
    height: 72px;
    padding: 5px;
    background: var(--white);
    border-radius: 5px;
    box-shadow: 0 6px 10px rgba(0, 30, 80, 0.45);
    text-decoration: none;
  }
  .cta__face {
    display: flex;
    align-items: center;
    justify-content: center;
    width: 100%;
    height: 100%;
    border: 2px solid var(--button-rim);
    background: linear-gradient(var(--button-top), var(--button-bottom));
    font-family: "Arimo", "Arial", sans-serif;
    font-size: 23px;
    color: var(--white);
    white-space: nowrap;
  }
  .cta__strong { font-weight: 700; margin-left: 6px; }
  .mascot {
    position: absolute;
    left: 890px;
    top: 72px;
    width: 190px;
    height: 400px;
    border-radius: 80px 80px 20px 20px;
    background: linear-gradient(var(--figure-top) 0%, var(--figure-top) 55%, var(--figure-bottom) 60%, var(--figure-bottom) 100%);
    opacity: 0.9;
  }
</style>
</head>
<body>
  <main class="banner">
    <svg class="banner__waves" viewBox="0 0 1200 485" aria-hidden="true">
      <path d="M0 330 C 250 250, 520 380, 780 330 S 1100 250, 1200 300" fill="none" stroke="rgba(255,255,255,0.35)" stroke-width="6"/>
      <path d="M0 400 C 300 330, 560 450, 820 380 S 1120 320, 1200 360" fill="none" stroke="rgba(255,255,255,0.45)" stroke-width="10"/>
      <path d="M420 485 C 620 380, 900 360, 1200 410 L 1200 485 Z" fill="rgba(255,255,255,0.18)"/>
      <path d="M520 470 C 720 390, 960 380, 1200 430" fill="none" stroke="rgba(255,255,255,0.6)" stroke-width="4"/>
    </svg>

    <h1 class="headline">
      <span class="headline__lead">Lesson</span>
      <span class="headline__tail">Learned</span>
    </h1>

    <p class="tagline">I will do it <span class="tagline__accent">better</span> if I have to do it <span class="tagline__accent">again</span>....</p>

    <a class="cta" href="#">
      <span class="cta__face">Click here to learn more about<span class="cta__strong">Lesson Learned</span></span>
    </a>

    <div class="mascot" role="img" aria-label="Cartoon employee in shirt and tie, smiling and pointing up at the headline"></div>
  </main>
</body>
</html>
```